Security Officer Training Certifications POSTCARD

We need Post Card Design
-Front and Back
-In Compliance with BRAMBLE INK for upload!
-For Oversized and Jumbo Size Cards (bramble inks)

Our Company:
www.patrolcraftacademyhubzone.org (FOR IDEAS)

We provide Corporate Security Officer/Criminal Justice/Police Tactics Training for Private Companies that have a security department and officers.

We provide:
Handcuffing certifications
Pepper Spray
Compliance Training
Instructor Training
California Guard Card

FRONT DESIGN TO BE VERY CATCH!
Back of Card List of Services/Menu

Our Card to display powerful image for a Security Officer Department
Traits in Pic and Deigns
VALUE
COMPETITIVE EDGE
PROFESSIONAL GROWTH
QUALITY
PROFICIENT/EFFECTIVE SECURITY OFFICERS
TACTICAL OFFICERS
PROFESSIONALISM
EXPERTS
INDUSTRY LEADERS
READINESS

Target Market(s)

Proprietary Security Officer Department. Agencies that hire their own guard force.
It will be owners of security guard companies, Security Directors, manager

Industry/Entity Type

Security

Requirements
Must have
• GREAT FROM OF CARD PICTURE that encompasses
• Corporate Security Officers
• MUST HAVE A COOL LOOK!
• Professionalism
• Tactical
• The best
• Upgrade skills
• BACK of Card:
• Like list of services with pics and cool stuff
• PICS of Security Officer /Police Professionals
• with great backgrounds!
• COOL
• BACK OF CARD
• Space to have address of receipient
• space for post age
• in ACCORDANCE with BRAMBLE INKS to upload...

```html
<!DOCTYPE html>
<html lang="en">
<head>
<meta charset="utf-8">
<title>Security Officer Training Postcard</title>
<link rel="stylesheet" href="https://fonts.googleapis.com/css2?family=Oswald:wght@500;600;700&family=Open+Sans:wght@400;600&display=swap">
<style>
:root{
  --backdrop:#b38f5a;
  --navy:#2b3a8f;
  --royal:#2a3f9e;
  --sky:#0b80c6;
  --cyan:#2aa3e0;
  --ink:#000;
  --white:#fff;
  --panel:#e6e7e8;
  --text-grey:#3a3a3a;
  --teal:#3f8aa3;
}
*{box-sizing:border-box;margin:0;padding:0}
html,body{width:934px;height:1200px;overflow:hidden;background:var(--backdrop)}
body{position:relative;font-family:"Open Sans",sans-serif}
.card{position:absolute;width:731px;height:474px;overflow:hidden;box-shadow:3px 4px 6px rgba(0,0,0,.35)}
.abs{position:absolute}

/* FRONT */
.front{left:105px;top:118px;background:var(--ink)}
.front-header{left:0;top:0;width:731px;height:128px;background:linear-gradient(90deg,var(--sky) 0%,#1b62b3 45%,var(--navy) 100%)}
.brand-mark{display:flex;align-items:center;justify-content:center;border-radius:50%;background:var(--white);text-align:center;font-family:"Oswald",sans-serif;font-weight:600;color:var(--navy);line-height:1.15;text-transform:uppercase}
.front .brand-mark{left:35px;top:14px;width:132px;height:132px;font-size:15px}
.headline{left:193px;top:30px;font-family:"Oswald",sans-serif;font-weight:600;color:var(--white);font-size:30px;line-height:40px;letter-spacing:.4px}
.hero-photo{left:455px;top:128px;width:276px;height:303px;background:radial-gradient(ellipse at 60% 45%,#5a4434 0%,#2a1d15 45%,#000 85%)}
.intro{left:34px;top:158px;width:440px;font-family:"Oswald",sans-serif;font-weight:500;color:var(--white);font-size:18.5px;line-height:25px;letter-spacing:.2px}
.provide-title{left:34px;top:245px;font-family:"Oswald",sans-serif;font-weight:600;color:var(--cyan);font-size:21px}
.bullets{list-style:none}
.bullets li{position:relative;padding-left:19px;height:22.4px;line-height:22.4px}
.bullets li::before{content:"";position:absolute;left:0;top:7px;width:10px;height:10px;border-radius:50%;background:radial-gradient(circle at 35% 35%,#f2f2f2,#8d8d8d)}
.provide-list{left:34px;top:280px;color:var(--white);font-size:17px}
.value-box{left:291px;top:256px;width:122px;height:161px;border-radius:6px;background:rgba(63,138,163,.92);border:1px solid #6fb0c6;padding:6px 10px;font-family:"Oswald",sans-serif;color:var(--white)}
.value-box .lead{font-size:18px;font-weight:600;line-height:21px;padding-bottom:4px;border-bottom:1px solid #1f5a70}
.value-box .perks{margin-top:4px;font-size:11.5px;font-weight:600;line-height:16.3px}
.contact-panel{left:0;top:405px;width:242px;height:69px;background:var(--panel);clip-path:polygon(0 0,100% 0,79% 100%,0 100%)}
.contact-panel .addr{position:absolute;left:34px;top:5px;font-size:12.5px;line-height:15.5px;color:#222}
.contact-panel .call{position:absolute;left:34px;top:37px;font-family:"Oswald",sans-serif;font-weight:600;font-size:20px;color:#2b2b2b}
.web-bar{left:215px;top:431px;width:516px;height:43px;background:var(--royal);clip-path:polygon(5% 0,100% 0,100% 100%,0 100%)}
.web-bar span{position:absolute;left:37px;top:4px;font-family:"Oswald",sans-serif;font-weight:600;font-size:22px;letter-spacing:1px;color:var(--white)}

/* BACK */
.back{left:103px;top:628px;background:var(--white)}
.photo{top:30px;height:118px}
.photo-a{left:38px;width:160px;background:linear-gradient(135deg,#6b7b5a,#1d2a3a)}
.photo-b{left:202px;width:121px;background:linear-gradient(160deg,#4f7a3a,#12161c)}
.photo-c{left:328px;width:134px;background:linear-gradient(180deg,#9cc06a,#6f9a3e)}
.photo-d{left:466px;width:121px;background:linear-gradient(90deg,#cfe0ea,#2c3f78)}
.postage{left:613px;top:10px;width:106px;height:106px;background:var(--panel);display:flex;align-items:center;justify-content:center;text-align:center;font-size:13.5px;line-height:17px;color:#111}
.info-band{left:0;top:148px;width:731px;height:27px;background:var(--royal)}
.info-band span{position:absolute;left:36px;top:1px;font-family:"Oswald",sans-serif;font-weight:600;font-size:17px;color:var(--white);letter-spacing:.2px}
.services-title{left:36px;top:187px;font-family:"Oswald",sans-serif;font-weight:600;color:var(--navy);font-size:21px}
.services-list{left:36px;top:221px;color:var(--text-grey);font-size:16.5px}
.back .brand-mark{left:324px;top:210px;width:136px;height:136px;font-size:15px;border:3px solid var(--navy)}
.back-addr{left:290px;top:358px;width:204px;text-align:center;font-size:11.5px;line-height:14.5px;color:var(--royal)}
.address-area{left:506px;top:207px;width:233px;height:202px;background:var(--panel)}
.address-area span{position:absolute;left:0;width:100%;top:52px;text-align:center;font-size:13.5px;color:#111}
.barcode-area{left:338px;top:409px;width:402px;height:52px;background:var(--panel)}
.barcode-area span{position:absolute;left:0;width:100%;top:17px;text-align:center;font-size:13.5px;color:#111}
</style>
</head>
<body>

<section class="card front" aria-label="Postcard front">
  <div class="abs front-header"></div>
  <div class="abs brand-mark">Northgate<br>Skills<br>Institute</div>
  <h1 class="abs headline">Security Guard Training in Los Angeles<br>CALIFORNIA GUARD CARD SPECIALISTS</h1>
  <div class="abs hero-photo" role="img" aria-label="Photo of a security officer in dark sunglasses touching an earpiece"></div>
  <p class="abs intro">We provide Corporate Security Officer / Criminal Justice/Police Tactics Training for private companies that have a security department and officers.</p>
  <h2 class="abs provide-title">We Provide:</h2>
  <ul class="abs bullets provide-list">
    <li>Handcuffing certifications</li>
    <li>Pepper Spray</li>
    <li>Compliance Training</li>
    <li>Instructor Training</li>
    <li>California Guard Card</li>
  </ul>
  <div class="abs value-box">
    <div class="lead">We make your training affordable!</div>
    <div class="perks">CONVENIENT<br>FAST<br>JOB PLACEMENT<br>COMPLIANCE<br>VALUABLE</div>
  </div>
  <div class="abs contact-panel">
    <div class="addr">1820 Harbor Crest Ave<br>Lakemont, CA 90199</div>
    <div class="call">Call: (555) 014-2297</div>
  </div>
  <div class="abs web-bar"><span>www.patrolcraftacademyhubzone.org</span></div>
</section>

<section class="card back" aria-label="Postcard back">
  <div class="abs photo photo-a" role="img" aria-label="Photo of a security officer in a cap speaking into a radio"></div>
  <div class="abs photo photo-b" role="img" aria-label="Photo of a security officer from behind near a gate"></div>
  <div class="abs photo photo-c" role="img" aria-label="Photo of an officer walking a patrol dog on grass"></div>
  <div class="abs photo photo-d" role="img" aria-label="Photo of an officer's duty belt with baton"></div>
  <div class="abs postage">Postage<br>Area</div>
  <div class="abs info-band"><span>For more information about our services, Please Call us Now: (555) 014-2297</span></div>
  <h2 class="abs services-title">Our Services</h2>
  <ul class="abs bullets services-list">
    <li>Value</li>
    <li>Competitive Edge</li>
    <li>Professional Growth</li>
    <li>Quality</li>
    <li>Proficient/effective Security Officers</li>
    <li>Tactical Officers</li>
    <li>Professionalism</li>
    <li>Experts</li>
    <li>Industry Leaders</li>
    <li>Readiness</li>
  </ul>
  <div class="abs brand-mark">Northgate<br>Skills<br>Institute</div>
  <div class="abs back-addr">1820 Harbor Crest Ave<br>Lakemont, CA 90199</div>
  <div class="abs address-area"><span>Address Area</span></div>
  <div class="abs barcode-area"><span>Barcode Area</span></div>
</section>

</body>
</html>
```